Innovative website for online education
Must be suitable to host classes, receive homework submissions, and sell products
Innovative website for online education - Education
Creative Brief
Education
handlearnly.com
Currently, HandLearnly sells a complete ASL DVD course. We are looking to update our website to appeal to universities, high schools, and families who buy our course for academic credit, certification preparation, or to communicate with friends and family. Within the year, our course will be completely rewritten and refilmed and formatted to be an online class at a university level. We will still provide a DVD course for purchase as well as supplemental materials.
University-type websites appeal to us like qrv.edu, as do unique menu bars (opposed to straightforward page navigation buttons across the top or side of the website). We do not like template-looking websites with "wallpaper" on either side behind the center "content banner" like pellwin.edu or tolbrook.edu
Modern
Maroon/red (like our logo)
Silver
Gray or white
below header
http://ravelmoorstudio.com/pim-dorsey
http://www.tarnbeacon.com/
http://lorcavine.com/#\Welcome
http://brisketfen.org/topeight/ Click "Finalists" at the bottom left, I like the diagonal expanding slides. http://www.quillor.com/design/40-websites-with-unusual-navigation.html has cool ideas. We want something unique and innovative, but not "artsy." It has to look professional, not like a scrapbook. I really like sliding page navigations and slide expanding navigations! I also like diagonals, but I'm not restricted to that if something else looks better. Also, I'm not extremely set on where the navigation must be but what I absolutely don't want is a bar down the left or right side like ours currently is now. Top, bottom, above or below header, or arranged creatively around the home page, that's all fine with me.
Marvelquist Marvelquist
Thank you for your patience regarding my business trip. I have contacted Pexalune to find a solution to the project being unveiled during this decision process and they have agreed to extend the project for 48 hours so we can finalize a design and so your designs will be protected. Thank you again to all the designers who participated in this project! Other than all the interruptions and complications on my side, I have been very pleased with the process and appreciate everyone's professionalism and patience.
Pexalune has such great customer service and extended my project for me. :) So it looks like the project will continue business trip or not. I will do my best to provide feedback while I am away. Thanks!
I will be extending the project one more time to give everyone a chance to respond to my feedback. However, I will be on a business trip for the next three days, so I will wait to reopen the project until the end of the weekend. Thank you.
I didn't realize when I started this project how much of a grasp I would need to have on what I wanted the website to be. I guess I just thought it would be similar to the logo contest and I would just pick something I liked. Lol. Obviously, this is way more complex and it has taken me some time to get my thoughts together about this project. I apologize for the delay; I definitely started this project too soon. I feel more prepared now that I've taken time to put together my ideas. Thank you all for your patience. I think we'd like to go for a home page that doesn't involve scrolling (or just minimal scrolling), sort of a whole page look. I still like the four-panel sliding navigation window, but it should take up all or most of the window. A more basic navigation bar can be at the top or bottom or not at all. The four sections we need will be "About," (though I would prefer a different word choice, I just haven't thought of one), "Courses," "Teachers," and "Students." If other navigation options are included, it will be things like "Results," and "Support." Another option could be having a main background image (with info video and brief "Who we are," with the other three options "Courses," "Teachers," and "Students" as navigation options on the page. I may or may not want a site map at the bottom of the page. I know that's helpful and common, but at the same time, it involves scrolling (which maybe that's just a personal preference of my own, but I like seeing everything at once.) I also want to apologize for these group updates instead of personal feedback, maybe now that I've mentally pinned down what I'm looking for, I'll be able to offer more personal feedback. Again, I'm sorry I started this project before I fully understood the scope of what I was doing! p.s. I am going to try to upload a Zentrova Paper Writer document that gives my very unprofessional "site map" in case it would be helpful. If it doesn't upload, I'll put it on StashBin or something and let you know. I have no idea if it will be helpful to a designer, but it helped me know what the big picture is.
I'm struggling with this. Sorry for the repeat posts!
I want to let everyone know that we will be extending the project at least once. I apologize for any inconvenience and I also want to apologize for not responding with feedback. Several circumstances have kept me from monitoring the project like I expected. I hope to reopen it sometime this week (hopefully sooner than later) and I hope to be more involved. Thank you to everyone who is participating, thank you for your work and your patience. I hope you will be understanding. I also want to apologize for not communicating my situation sooner than now. Each day, I kept thinking we were almost back to normal, but things kept coming up. I'm going to give it another day or two to make sure things are under control and then I will reopen the project. Regards
Thank you to everyone who has submitted designs! So far, I really like the designs that are wide rather than narrow banner-type. I also like the designs that use diagonals, especially incorporated in the sliding navigation like one of my example websites used. Also, shorter pages are better since we don't currently have a lot of content. I also like the easy-to-navigate look of a short page; I personally like not having to scroll down very far to reach the bottom. I am meeting with my business partner to discuss the particular navigation buttons or inner page links we need to have included on the home page. I will be sure to post them here so you guys aren't having to come up with navigation topics. I'm sorry about that, it's something I didn't even think about until I saw such a wide variety. =) One of the main questions we will determine is if we want to go ahead and lay it out in preparation for online learning or just keep it a product page for now. Thanks and I look forward to seeing more designs! I'll try to be more frequent in my feedback.

```html
<!DOCTYPE html>
<html lang="en">
<head>
<meta charset="utf-8">
<title>HandLearnly – Communication for Everyone</title>
<link href="https://fonts.googleapis.com/css2?family=Lato:wght@400;700;900&family=Lora:ital@1&display=swap" rel="stylesheet">
<style>
  :root{
    --maroon:#c4161c;
    --maroon-dark:#8e0f13;
    --ink:#0d0d0d;
    --panel:#1d1d1d;
    --panel-hi:#262626;
    --silver:#c8c8c8;
    --text:#e9e9e9;
    --muted:#9a9a9a;
    --line:#5a5a5a;
  }
  *{box-sizing:border-box;margin:0;padding:0}
  html,body{width:1200px;height:797px;overflow:hidden;background:var(--ink)}
  body{font-family:"Lato",Arial,sans-serif;color:var(--text);position:relative}

  .hero-backdrop{position:absolute;inset:0 0 48px 0;
    background:
      radial-gradient(ellipse 38% 55% at 72% 55%, rgba(120,105,100,.55), transparent 70%),
      radial-gradient(ellipse 30% 40% at 60% 70%, rgba(190,160,145,.35), transparent 70%),
      linear-gradient(180deg,#2a2a2a 0%,#161616 45%,#0e0e0e 100%);}
  .header-band{position:absolute;left:0;top:0;width:1200px;height:128px;
    background:linear-gradient(180deg,rgba(60,60,60,.75),rgba(20,20,20,.55));}

  .brand{position:absolute;left:132px;top:34px}
  .brand-name{font-weight:900;font-size:58px;letter-spacing:-1px;color:var(--maroon);line-height:1}
  .brand-tag{font-size:15px;color:var(--silver);margin-top:2px;letter-spacing:.3px}

  .login{position:absolute;top:17px;height:24px;font-size:11px;font-weight:700;letter-spacing:.4px;
    display:flex;align-items:center;justify-content:center;text-transform:uppercase}
  .login-teachers{left:787px;width:125px;border:1px solid var(--silver);color:var(--text)}
  .login-students{left:919px;width:120px;background:var(--maroon);color:#fff}

  .main-nav{position:absolute;left:523px;top:86px;width:540px;border-bottom:1px solid var(--line);
    display:flex;justify-content:space-between;padding:0 4px 12px}
  .main-nav a{color:var(--text);text-decoration:none;font-size:16px;font-weight:400;position:relative}
  .main-nav a.is-active{font-weight:700}
  .main-nav a.is-active::after{content:"";position:absolute;left:0;right:0;bottom:-14px;height:4px;background:var(--maroon)}

  .video{position:absolute;left:132px;top:149px;width:516px;height:295px;background:#fff;border:1px solid #444}
  .video-still{position:absolute;left:0;top:0;width:100%;height:265px;
    background:radial-gradient(ellipse 45% 55% at 45% 55%,#b71c22 0%,#7c1014 45%,#f4f4f4 75%)}
  .video-controls{position:absolute;left:0;bottom:0;width:100%;height:30px;background:#111;display:flex;align-items:center;gap:10px;padding:0 10px;font-size:12px;color:#ddd}
  .progress{flex:1;height:4px;background:#555;position:relative}
  .progress::before{content:"";position:absolute;left:0;top:0;height:100%;width:30%;background:var(--maroon)}
  .hd{font-weight:900;font-style:italic}

  .slider-arrow{position:absolute;top:402px;width:60px;height:60px;border-radius:50%;border:2px solid #888;background:rgba(0,0,0,.35)}
  .slider-arrow svg{width:100%;height:100%}
  .arrow-prev{left:28px}.arrow-next{left:1043px}

  .hero-name{position:absolute;left:276px;top:470px;font-weight:700;font-size:30px;color:var(--text)}
  .hero-tagline{position:absolute;left:149px;top:508px;font-family:"Lora",Georgia,serif;font-style:italic;font-size:25px;color:var(--text)}

  .panels{position:absolute;left:132px;top:559px;width:936px;height:162px}
  .panel{position:absolute;top:0;height:162px;padding:28px 0 0}
  .panel-bg{position:absolute;inset:0;width:100%;height:100%}
  .panel-courses{left:0;width:340px}
  .panel-teachers{left:310px;width:340px;top:-4px;height:170px}
  .panel-students{left:620px;width:316px}
  .panel-body{position:relative;display:flex;gap:16px}
  .panel-icon{width:48px;height:48px;margin-top:36px;flex:none}
  .panel h2{font-size:18px;font-weight:700;color:#fff;margin-bottom:14px}
  .panel p{font-size:13px;line-height:1.35;color:var(--text);width:190px}
  .read-more{display:block;margin-top:10px;font-size:12px;color:var(--maroon);text-decoration:none;font-weight:700}

  .site-footer{position:absolute;left:0;top:749px;width:1200px;height:48px;background:#0a0a0a;border-top:1px solid #262626;
    display:flex;align-items:center;font-size:14px;color:var(--silver)}
  .contact{position:absolute;display:flex;align-items:center;gap:8px}
  .contact-phone{left:132px}.contact-mail{left:264px}
  .copyright{position:absolute;left:532px;font-size:13px}
  .social{position:absolute;left:922px;display:flex;gap:10px}
  .social span{width:30px;height:30px;border-radius:50%;background:#e6e6e6;display:block}
</style>
</head>
<body>
  <div class="hero-backdrop" role="img" aria-label="Dark backdrop photo of a person in a knit sweater forming a sign with both hands"></div>
  <div class="header-band"></div>

  <header>
    <div class="brand">
      <div class="brand-name">HandLearnly</div>
      <div class="brand-tag">Communication for Everyone</div>
    </div>
    <a class="login login-teachers">Teachers Login</a>
    <a class="login login-students">Students Login</a>
    <nav class="main-nav">
      <a class="is-active" href="#">ABOUT</a>
      <a href="#">COURSES</a>
      <a href="#">TEACHERS</a>
      <a href="#">STUDENTS</a>
      <a href="#">RESULTS</a>
      <a href="#">SUPPORT</a>
    </nav>
  </header>

  <section class="video">
    <div class="video-still" role="img" aria-label="Video still of the DVD course box set and discs"></div>
    <div class="video-controls">
      <svg width="10" height="12" viewBox="0 0 10 12"><path d="M0 0L10 6L0 12Z" fill="#ddd"/></svg>
      <div class="progress"></div>
      <span>1:26 / 4:02</span>
      <svg width="14" height="12" viewBox="0 0 14 12"><path d="M0 4h3l4-4v12l-4-4H0z" fill="#ddd"/></svg>
      <span class="hd">HD</span>
    </div>
  </section>

  <a class="slider-arrow arrow-prev" href="#"><svg viewBox="0 0 60 60"><path d="M34 19L23 30L34 41" fill="none" stroke="#ddd" stroke-width="3"/></svg></a>
  <a class="slider-arrow arrow-next" href="#"><svg viewBox="0 0 60 60"><path d="M26 19L37 30L26 41" fill="none" stroke="#ddd" stroke-width="3"/></svg></a>

  <div class="hero-name">HandLearnly</div>
  <p class="hero-tagline">End the silence... The power is in your hands.</p>

  <section class="panels">
    <article class="panel panel-courses">
      <svg class="panel-bg" viewBox="0 0 340 162" preserveAspectRatio="none"><polygon points="0,0 340,0 310,162 0,162" fill="rgba(29,29,29,.92)"/></svg>
      <div class="panel-body" style="padding-left:20px">
        <svg class="panel-icon" viewBox="0 0 48 48"><rect x="8" y="12" width="32" height="20" fill="none" stroke="#fff" stroke-width="3"/><path d="M3 36h42l-3 4H6z" fill="#fff"/></svg>
        <div><h2>COURSES</h2><p>Lorem ipsum dolor sitan amet consectetuer adipiscing elitra sed amtil diam volutpat.</p><a class="read-more" href="#">Read more &gt;</a></div>
      </div>
    </article>
    <article class="panel panel-teachers">
      <svg class="panel-bg" viewBox="0 0 340 170" preserveAspectRatio="none"><polygon points="30,0 340,0 310,170 0,170" fill="rgba(38,38,38,.95)"/><line x1="30" y1="1.5" x2="340" y2="1.5" stroke="#c4161c" stroke-width="3"/><line x1="0" y1="168.5" x2="310" y2="168.5" stroke="#c4161c" stroke-width="3"/></svg>
      <div class="panel-body" style="padding-left:44px">
        <svg class="panel-icon" viewBox="0 0 48 48"><circle cx="24" cy="28" r="15" fill="#c4161c"/><path d="M24 13c1-4 4-7 8-7" stroke="#c4161c" stroke-width="3" fill="none"/></svg>
        <div><h2>TEACHERS</h2><p>Lorem ipsum dolor sitan amet consectetuer adipiscing elitra sed amtil diam volutpat.</p><a class="read-more" href="#">Read more &gt;</a></div>
      </div>
    </article>
    <article class="panel panel-students">
      <svg class="panel-bg" viewBox="0 0 316 162" preserveAspectRatio="none"><polygon points="30,0 316,0 316,162 0,162" fill="rgba(29,29,29,.92)"/></svg>
      <div class="panel-body" style="padding-left:40px">
        <svg class="panel-icon" viewBox="0 0 48 48"><path d="M4 14L24 6L44 14L24 22Z" fill="#fff"/><path d="M12 18v10c6 5 18 5 24 0V18L24 23z" fill="#fff"/><rect x="41" y="14" width="2" height="14" fill="#fff"/></svg>
        <div><h2>STUDENTS</h2><p>Lorem ipsum dolor sitan amet consectetuer adipiscing elitra sed amtil diam volutpat.</p><a class="read-more" href="#">Read more &gt;</a></div>
      </div>
    </article>
  </section>

  <footer class="site-footer">
    <div class="contact contact-phone">
      <svg width="12" height="16" viewBox="0 0 12 16"><rect x="1" y="0" width="10" height="16" rx="2" fill="#ccc"/><rect x="3" y="2" width="6" height="10" fill="#0a0a0a"/></svg>
      <span>800-555-0147</span>
    </div>
    <div class="contact contact-mail">
      <svg width="16" height="12" viewBox="0 0 16 12"><rect width="16" height="12" fill="#ccc"/><path d="M0 0L8 7L16 0" stroke="#0a0a0a" fill="none"/></svg>
      <span>contact@handlearnly.com</span>
    </div>
    <div class="copyright">Copyright © 2014 HandLearnly. All Right Reserved.</div>
    <div class="social" aria-label="Social links"><span></span><span></span><span></span><span></span></div>
  </footer>
</body>
</html>
```